Pumpkin Seed Oil Dark Green Plastic Bottle Needs a Label Design

We need a label design for an Slovenian tourist farm from an agricultural area called Prekmurje and known for its gourmet delicacies.

We would like to be presented with label designs for a 1 litre (approximately 33.814 U.S. fluid ounces) dark green plastic bottle containing undiluted (ie. 100%), viscous and very dark green (almost black) pumpkin seed oil. The label design should be consistent with nature and food processing industry, represent adequate colours, be 11 centimetres (approximately 4.331 inches) high and 7.5 centimetres (approximately 2.953 inches) wide and have enough blank/empty space (approximately 1/3 of the label) for the subsequently added legally stipulated text.

We look forward to receive visual and appealing label designs that ought to communicate quality, trust and, most importantly, the geographical indication/location/origin.

We would like to add that the said client has not yet worked on their corporate identity (colours, fonts ...) which means that ample freedom is allowed and should be taken advantage of.
Updates

Reason: We received merely 6 label designs while we expected to receive quite a few more. The provided task description remains the same.

Target Market(s)

Wider public and (small) retailers.

Industry/Entity Type

Agribusiness

Requirements
Must have
• Label design size: 11 centimetres (approximately 4.331 inches) x 7.5 centimetres (approximately 2.953 inches).
• Blank/empty space: approximately 1/3 of the label.
Nice to have
• Be visual.
• Communicate quality, trust and, most importantly, the geographical indication/location/origin.

```html
<!DOCTYPE html>
<html lang="en">
<head>
<meta charset="utf-8">
<title>Pumpkin Seed Oil Label</title>
<link rel="stylesheet" href="https://fonts.googleapis.com/css2?family=Noto+Sans:wght@400;700&display=swap">
<style>
  :root {
    --bg-green: #2a7c57;
    --label-white: #ffffff;
    --rule-green: #1f7a3c;
    --ink: #111111;
    --oil-green: #2e9a5c;
    --glass-grey: #d9dcda;
  }
  html, body {
    margin: 0;
    padding: 0;
    width: 764px;
    height: 1200px;
    overflow: hidden;
    background: var(--bg-green);
  }
  .canvas {
    position: relative;
    width: 764px;
    height: 1200px;
    background: var(--bg-green);
    font-family: "Noto Sans", Verdana, sans-serif;
    color: var(--ink);
  }
  .label {
    position: absolute;
    left: 178px;
    top: 300px;
    width: 413px;
    height: 597px;
    background: var(--label-white);
  }
  .title-word {
    position: absolute;
    margin: 0;
    font-weight: 700;
    font-size: 36px;
    line-height: 1;
  }
  .title-pumpkin { left: 31px; top: 42px; }
  .title-seed { left: 156px; top: 90px; }
  .title-oil { left: 250px; top: 138px; }
  .rule {
    position: absolute;
    height: 5px;
    background: var(--rule-green);
  }
  .rule-title { left: 46px; top: 186px; width: 260px; }
  .rule-intro { left: 46px; top: 352px; width: 324px; }
  .intro {
    position: absolute;
    left: 10px;
    right: 10px;
    top: 200px;
    margin: 0;
    text-align: center;
    font-size: 27px;
    line-height: 34px;
  }
  .intro .delicacies { text-decoration: underline; text-underline-offset: 3px; }
  .jug-art {
    position: absolute;
    left: 13px;
    top: 367px;
    width: 120px;
    height: 212px;
    background: linear-gradient(to bottom, var(--glass-grey) 0%, var(--label-white) 40%, var(--oil-green) 70%, var(--oil-green) 100%);
  }
  .sector {
    position: absolute;
    left: 140px;
    top: 512px;
    margin: 0;
    font-weight: 700;
    font-size: 27px;
    line-height: 1;
  }
</style>
</head>
<body>
  <div class="canvas">
    <section class="label">
      <h1 class="title-word title-pumpkin">Pumpkin</h1>
      <h1 class="title-word title-seed">Seed</h1>
      <h1 class="title-word title-oil">Oil</h1>
      <div class="rule rule-title"></div>
      <p class="intro">Slovenian tourist farm from an agricultural area called Prekmurje known for its <span class="delicacies">gourmet delicacies.</span></p>
      <div class="rule rule-intro"></div>
      <div class="jug-art" role="img" aria-label="Glass jug filled with green pumpkin seed oil, with a few pumpkin seeds"></div>
      <p class="sector">Agribusiness</p>
    </section>
  </div>
</body>
</html>
```